Kestrel Electrical Business Card

We need a business card design for our family-run electrical contracting business based in Western Australia called 'Kestrel Electrical'. We provide electrical services including residential, commercial and industrial. We aim for individual business cards to be made for all of our employees. We already have a company logo, which we require to be featured on the design. We would like simple, sleek and vibrant designs, which incorporate our logo and represent our business. We do not want anything involving too many graphics/images. We like the colours red, black, white and all shades of grey. The final design should communicate professionalism and trustworthiness.
We require the following contact information:
Name- Owen Strickland
EC 5809
Mobile number- 0455 918 302
Fax number (including area code)- (08) 9640 2718
Email adress- name@kestrelelectrical.example
Electrical
- ITC Handel Bold

```html
<!DOCTYPE html>
<html lang="en">
<head>
<meta charset="utf-8">
<title>Kestrel Electrical Business Card</title>
<link rel="stylesheet" href="https://fonts.googleapis.com/css2?family=Saira:wght@400;500;700&display=swap">
<style>
  :root {
    --backdrop: #d9d9d9;
    --card-white: #f7f7f7;
    --brand-red: #e3262b;
    --brand-red-deep: #c9161c;
    --ink: #1f1f1f;
    --on-red: #ffffff;
  }
  * { box-sizing: border-box; margin: 0; padding: 0; }
  html, body {
    width: 1200px;
    height: 1023px;
    overflow: hidden;
    background: var(--backdrop);
    font-family: "Saira", sans-serif;
  }
  .card {
    position: absolute;
    left: 100px;
    top: 226px;
    width: 1000px;
    height: 572px;
    background: var(--card-white);
    box-shadow: 0 18px 40px rgba(0,0,0,0.25);
    overflow: hidden;
  }
  .card__header {
    position: absolute;
    inset: 0 0 auto 0;
    height: 220px;
    display: flex;
    align-items: center;
    padding-left: 70px;
    gap: 26px;
  }
  .brand__mark {
    width: 64px;
    height: 64px;
    background: var(--brand-red);
  }
  .brand__name {
    font-weight: 700;
    font-size: 64px;
    letter-spacing: 1px;
    color: var(--ink);
    text-transform: uppercase;
    line-height: 1;
  }
  .card__body {
    position: absolute;
    inset: 220px 0 0 0;
    background: linear-gradient(160deg, var(--brand-red) 0%, var(--brand-red-deep) 100%);
    color: var(--on-red);
  }
  .person {
    position: absolute;
    left: 70px;
    bottom: 70px;
  }
  .person__name {
    font-weight: 700;
    font-size: 44px;
    line-height: 1.1;
  }
  .person__licence {
    font-weight: 500;
    font-size: 28px;
    margin-top: 10px;
  }
  .contacts {
    position: absolute;
    right: 70px;
    top: 62px;
    list-style: none;
    display: flex;
    flex-direction: column;
    gap: 26px;
  }
  .contact {
    display: flex;
    align-items: center;
    gap: 20px;
    font-size: 26px;
    font-weight: 500;
    letter-spacing: 0.5px;
  }
  .contact__icon {
    width: 54px;
    height: 54px;
    flex: none;
  }
</style>
</head>
<body>
  <article class="card">
    <header class="card__header">
      <span class="brand__mark" aria-hidden="true"></span>
      <span class="brand__name">Kestrel Electrical</span>
    </header>
    <section class="card__body">
      <div class="person">
        <p class="person__name">Owen Strickland</p>
        <p class="person__licence">EC 5809</p>
      </div>
      <ul class="contacts">
        <li class="contact">
          <svg class="contact__icon" viewBox="0 0 54 54" aria-label="Mobile">
            <circle cx="27" cy="27" r="25" fill="none" stroke="#fff" stroke-width="3"/>
            <rect x="19" y="13" width="16" height="28" rx="3" fill="#fff"/>
            <rect x="22" y="17" width="10" height="16" fill="#e3262b"/>
          </svg>
          <span>0455 918 302</span>
        </li>
        <li class="contact">
          <svg class="contact__icon" viewBox="0 0 54 54" aria-label="Fax">
            <circle cx="27" cy="27" r="25" fill="none" stroke="#fff" stroke-width="3"/>
            <rect x="19" y="13" width="16" height="10" fill="#fff"/>
            <rect x="13" y="22" width="28" height="16" rx="2" fill="#fff"/>
            <rect x="18" y="33" width="18" height="3" fill="#e3262b"/>
          </svg>
          <span>(08) 9640 2718</span>
        </li>
        <li class="contact">
          <svg class="contact__icon" viewBox="0 0 54 54" aria-label="Email">
            <circle cx="27" cy="27" r="25" fill="none" stroke="#fff" stroke-width="3"/>
            <rect x="14" y="18" width="26" height="18" fill="none" stroke="#fff" stroke-width="2.5"/>
            <polyline points="14,18 27,29 40,18" fill="none" stroke="#fff" stroke-width="2.5"/>
          </svg>
          <span>name@kestrelelectrical.example</span>
        </li>
      </ul>
    </section>
  </article>
</body>
</html>
```